New Label Design Project

I need a coffee label that i can edit based on the designs we first came up with. The coffee bags i will use are 250g side gusseted Matt black so it can capture the colours in the logos.. My issue is that i need to add information regarding the type of coffee I am selling - Im using 5 single origin sourced coffee and the beans are all 100% arabica and ill add some information on the current stock I’m using… Im out of ideas at the moment! but want to keep it clean and fresh… Information I must have is weight… 250g and roasted on date (best used within 3 months of date). anything else will be considered?! Ill attached the logos / references and also the website which is still under development… www.nqcoffee.co.uk

```html
<!DOCTYPE html>
<html lang="en">
<head>
<meta charset="utf-8">
<title>Northquay Roastery Coffee – 250g Pouch Labels</title>
<link rel="stylesheet" href="https://fonts.googleapis.com/css2?family=Questrial&family=Cormorant+Garamond:ital,wght@1,500&family=Oswald:wght@500&display=swap">
<style>
  :root {
    --backdrop: #847d77;
    --pouch: #121212;
    --gold: #c98a4b;
    --gold-dark: #8f5b2c;
    --gold-light: #e0a265;
    --cream: #e8d7bf;
    --ink: #1a130c;
    --band: linear-gradient(90deg, var(--gold-dark) 0%, var(--gold) 35%, var(--gold-light) 55%, var(--gold) 75%, var(--gold-dark) 100%);
  }
  * { box-sizing: border-box; margin: 0; padding: 0; }
  html, body { width: 1200px; height: 1200px; overflow: hidden; }
  body {
    background: var(--backdrop);
    font-family: "Questrial", sans-serif;
    position: relative;
  }
  .pouch {
    position: absolute;
    top: 274px;
    width: 460px;
    height: 674px;
    background: var(--pouch);
    color: var(--gold);
  }
  .pouch--front { left: 116px; }
  .pouch--back { left: 680px; }

  .rule { position: absolute; left: 0; right: 0; height: 3px; background: var(--band); }
  .band {
    position: absolute; left: 0; right: 0;
    background: var(--band);
    color: var(--ink);
    display: flex; align-items: center;
  }

  /* front */
  .pouch--front .rule--a { top: 36px; }
  .pouch--front .band { top: 48px; height: 38px; padding-left: 30px; font-size: 22px; gap: 20px; }
  .pouch--front .band .tagline { font-size: 18px; }
  .pouch--front .rule--b { top: 96px; }

  .badge {
    position: absolute; left: 106px; top: 182px;
    width: 240px; height: 240px;
    border: 5px solid var(--gold);
    border-radius: 50%;
    display: flex; flex-direction: column; align-items: center; justify-content: center;
    text-align: center;
    font-family: "Oswald", sans-serif;
    font-weight: 500;
    color: var(--gold);
    letter-spacing: 2px;
  }
  .badge .brand-name { font-size: 34px; line-height: 1.1; }
  .badge .brand-sub { font-size: 16px; margin-top: 4px; }
  .badge .origin { font-size: 14px; margin-top: 18px; line-height: 1.4; }

  .product-line {
    position: absolute; left: 0; right: 0; top: 470px;
    text-align: center; font-size: 30px; letter-spacing: 0.5px;
  }
  .product-claim {
    position: absolute; left: 0; right: 0; top: 510px;
    text-align: center; font-size: 42px;
  }
  .diet-mark {
    position: absolute; left: 40px; top: 590px;
    display: flex; flex-direction: column; gap: 3px;
    font-size: 7px; line-height: 1.2; color: var(--gold);
  }
  .diet-mark .icon {
    width: 30px; height: 20px; margin-left: 8px;
    background: linear-gradient(135deg, var(--gold-light), var(--gold-dark));
    border-radius: 0 14px 0 14px;
  }
  .diet-mark .label { border-bottom: 1px solid var(--gold); padding-bottom: 2px; text-transform: uppercase; }

  .net-weight {
    position: absolute; right: 30px; top: 598px;
    text-align: right; font-size: 15px; line-height: 1.25;
  }

  /* back */
  .pouch--back .rule--a { top: 26px; }
  .pouch--back .band { top: 40px; height: 34px; }
  .pouch--back .rule--b { top: 84px; }

  .brand-lockup {
    position: absolute; left: 0; right: 0; top: 124px;
    display: flex; flex-direction: column; align-items: center;
    font-family: "Oswald", sans-serif; font-weight: 500;
    color: var(--cream); letter-spacing: 2px;
  }
  .brand-lockup .brand-name { font-size: 28px; line-height: 1.1; }
  .brand-lockup .brand-sub { font-size: 11px; letter-spacing: 3px; margin-top: 4px; }

  .roast-name {
    position: absolute; left: 0; right: 0; top: 232px;
    text-align: center;
    font-family: "Cormorant Garamond", serif; font-style: italic; font-weight: 500;
    font-size: 56px;
  }
  .roast-notes {
    position: absolute; left: 20px; right: 20px; top: 322px;
    text-align: center; font-size: 21px; line-height: 1.28;
  }
  .freshness-tag {
    position: absolute; left: 130px; top: 456px;
    width: 204px; height: 32px;
    background: var(--band); border-radius: 5px;
    color: var(--ink); font-size: 20px; letter-spacing: 0.5px;
    display: flex; align-items: center; justify-content: center;
  }
  .freshness-note {
    position: absolute; left: 0; right: 0; top: 496px;
    text-align: center; font-size: 9px; line-height: 1.35;
  }
  .best-before {
    position: absolute; left: 0; right: 0; top: 548px;
    text-align: center; font-size: 10px; font-weight: 700;
  }
  .maker {
    position: absolute; left: 26px; top: 596px;
    font-size: 8px; line-height: 1;
  }
  .maker .origin-country { display: block; margin-top: 26px; text-transform: uppercase; font-weight: 700; }
  .pouch--back .net-weight { top: 592px; }
</style>
</head>
<body>

  <section class="pouch pouch--front" aria-label="Front label">
    <div class="rule rule--a"></div>
    <div class="band"><span>FRESH LOCK</span><span class="tagline">Resealable Strip to LOCK</span></div>
    <div class="rule rule--b"></div>

    <div class="badge">
      <span class="brand-name">NORTHQUAY</span>
      <span class="brand-sub">ROASTERY COFFEE</span>
      <span class="origin">HARBOURNE<br>ESTD 2018</span>
    </div>

    <p class="product-line">COFFEE and BEANS</p>
    <p class="product-claim">100% Arabica</p>

    <div class="diet-mark">
      <div class="icon" role="img" aria-label="Leaf icon"></div>
      <span>Suitable for</span>
      <span class="label">Vegans and Vegetarians</span>
    </div>

    <p class="net-weight">Net wt.<br>250g</p>
  </section>

  <section class="pouch pouch--back" aria-label="Back label">
    <div class="rule rule--a"></div>
    <div class="band"></div>
    <div class="rule rule--b"></div>

    <div class="brand-lockup">
      <span class="brand-name">NORTHQUAY</span>
      <span class="brand-sub">ROASTERY COFFEE</span>
    </div>

    <h2 class="roast-name">Smooth</h2>
    <p class="roast-notes">100% Arabica coffee beans in reach<br>taste and aroma of finely roasted,<br>A best cup&nbsp; just waiting to taste</p>

    <div class="freshness-tag">FRESH LOCK</div>
    <p class="freshness-note">Keep your coffee in this resealable pack<br>to ensure that you get a best cup<br>anytime, anywhere.</p>
    <p class="best-before">Best used with in 3 mos. of date</p>

    <p class="maker">Manufactured by:<span class="origin-country">Product of the UK</span></p>
    <p class="net-weight">Net wt.<br>250g</p>
  </section>

</body>
</html>
```